I need a newspaper ads that suits events / outings all over the world. refreshing feeling that suits my company logo.
Size of the ads is 6cm by 6cm a square
takenote
1) Joining up as members is free .
2) Places of interest tickets discount for members
3) Special events / outings host almost everyday
4) main point is everyone able to know each another
website : www.WanderNookly.com
Target Market(s)
Targeting general age 18-40 . mainly singles
contents to put inside the ads
2) Local Places of interest tickets discount for members
4) Website : www.WanderNookly.com
5) We also host photos contest
6) Meet the different faces of the world
7) Experience Sharing Gathering !
Industry/Entity Type
It Company
Requirements
Must have
- Refreshing feeling , and professional . will be uploading more pictures , kindly put some pictures combine into it to make people feel there is a lot activities can be involve when they join as member.

```html
<!DOCTYPE html>
<html lang="en">
<head>
<meta charset="utf-8">
<title>The Gate to the New World – Ad Variants</title>
<link href="https://fonts.googleapis.com/css2?family=Oswald:wght@400;500&family=PT+Sans+Narrow&display=swap" rel="stylesheet">
<style>
  :root {
    --board: #dbdcdd;
    --paper: #ffffff;
    --ink: #333333;
    --blue-light: #22a8dc;
    --blue-dark: #0b5e8e;
    --blue-band: #1883b8;
    --mono-dark: #1a1a1a;
    --mono-band: #707070;
    --logo-grey: #7a7a7a;
  }
  * { margin: 0; padding: 0; box-sizing: border-box; }
  html, body { width: 1200px; height: 900px; overflow: hidden; background: var(--board); }
  .board { position: relative; width: 1200px; height: 900px; }
  .ad {
    position: absolute; top: 279px; width: 343px; height: 343px;
    background: var(--paper); overflow: hidden;
  }
  .ad--colour { left: 243px; }
  .ad--mono { left: 615px; }
  .perks {
    position: absolute; left: 18px; top: 18px; width: 150px;
    list-style: none; font-family: "PT Sans Narrow", sans-serif;
    font-size: 9.6px; line-height: 10.6px; color: var(--ink);
  }
  .perks li { position: relative; padding-left: 6px; margin-bottom: 4.4px; }
  .perks li::before { content: "•"; position: absolute; left: 0; }
  .headline {
    position: absolute; left: 172px; top: 12px;
    font-family: "Oswald", sans-serif; font-weight: 500;
    font-size: 41px; line-height: 41px; letter-spacing: -0.5px;
    transform: scaleX(0.86); transform-origin: left top;
    white-space: nowrap;
  }
  .ad--colour .headline {
    background: linear-gradient(180deg, var(--blue-light), var(--blue-dark));
    -webkit-background-clip: text; background-clip: text; color: transparent;
  }
  .ad--mono .headline { color: var(--mono-dark); }
  .photo-band { position: absolute; left: 0; top: 137px; width: 343px; height: 160px; display: block; }
  .brand {
    position: absolute; left: 14px; top: 300px; display: flex; align-items: center; gap: 8px;
  }
  .brand-mark { width: 34px; height: 34px; border-radius: 50%; background: var(--logo-grey); }
  .brand-name {
    font-family: "PT Sans Narrow", sans-serif; font-size: 20px; line-height: 20px;
    color: var(--blue-dark); letter-spacing: 1px;
  }
  .ad--mono .brand-name { color: var(--logo-grey); }
  .website {
    position: absolute; right: 10px; top: 323px;
    font-family: "PT Sans Narrow", sans-serif; font-size: 11.5px; color: var(--ink);
  }
</style>
</head>
<body>
<div class="board">

  <section class="ad ad--colour">
    <ul class="perks">
      <li>Joining up as members is free</li>
      <li>Local Places of interest tickets discount for members</li>
      <li>Special events / outings host almost everyday</li>
      <li>We also host photos contest</li>
      <li>Meet the different faces of the world</li>
      <li>Experience Sharing Gathering !</li>
    </ul>
    <h1 class="headline">THE GATE<br>TO THE NEW<br>WORLD</h1>
    <svg class="photo-band" viewBox="0 0 343 160" aria-hidden="false">
      <defs>
        <linearGradient id="photoTonesColour" x1="0" y1="0" x2="0" y2="1">
          <stop offset="0" stop-color="#c9a58c"/>
          <stop offset="0.45" stop-color="#8a6a5a"/>
          <stop offset="1" stop-color="#3a3a42"/>
        </linearGradient>
      </defs>
      <path role="img" aria-label="Group photo of six smiling young friends standing arm in arm"
            d="M0 20 Q60 0 170 8 Q280 0 343 4 L343 140 Q250 120 150 112 Q60 108 0 118 Z"
            fill="url(#photoTonesColour)"/>
      <path d="M0 118 Q60 108 150 112 Q250 120 343 140 L343 148 Q250 128 150 122 Q60 118 0 126 Z" fill="var(--blue-band)"/>
      <path d="M0 126 Q60 118 150 122 Q250 128 343 148 L343 160 L0 160 Z" fill="var(--paper)"/>
    </svg>
    <div class="brand">
      <span class="brand-mark"></span>
      <span class="brand-name">ORBIVA EVENTS</span>
    </div>
    <p class="website">www.WanderNookly.com</p>
  </section>

  <section class="ad ad--mono">
    <ul class="perks">
      <li>Joining up as members is free</li>
      <li>Local Places of interest tickets discount for members</li>
      <li>Special events / outings host almost everyday</li>
      <li>We also host photos contest</li>
      <li>Meet the different faces of the world</li>
      <li>Experience Sharing Gathering !</li>
    </ul>
    <h1 class="headline">THE GATE<br>TO THE NEW<br>WORLD</h1>
    <svg class="photo-band" viewBox="0 0 343 160" aria-hidden="false">
      <defs>
        <linearGradient id="photoTonesMono" x1="0" y1="0" x2="0" y2="1">
          <stop offset="0" stop-color="#b8b8b8"/>
          <stop offset="0.45" stop-color="#7a7a7a"/>
          <stop offset="1" stop-color="#3a3a3a"/>
        </linearGradient>
      </defs>
      <path role="img" aria-label="Black and white group photo of six smiling young friends standing arm in arm"
            d="M0 20 Q60 0 170 8 Q280 0 343 4 L343 140 Q250 120 150 112 Q60 108 0 118 Z"
            fill="url(#photoTonesMono)"/>
      <path d="M0 118 Q60 108 150 112 Q250 120 343 140 L343 148 Q250 128 150 122 Q60 118 0 126 Z" fill="var(--mono-band)"/>
      <path d="M0 126 Q60 118 150 122 Q250 128 343 148 L343 160 L0 160 Z" fill="var(--paper)"/>
    </svg>
    <div class="brand">
      <span class="brand-mark"></span>
      <span class="brand-name">ORBIVA EVENTS</span>
    </div>
    <p class="website">www.WanderNookly.com</p>
  </section>

</div>
</body>
</html>
```